PR firm needs new podcast cover design

Our podcast is rebranding, and we need a new logo. Our podcast was previously called Ripple & Reason (logo attached), and the new name is Bright Ledger. We are a public relations and communications consulting firm, and we talk about current stories/issues in the PR industry.

We are open to keeping the yellow/black color scheme but we're also open to other ideas. We would like to new logo to be a little more visually appealing than the old one.

The look and feel should be strong, modern but professional. The text should say Bright Ledger and include the phrase "A podcast by Thornbury Communications." Please let us know if you have any questions about this project. Thank you!

```html
<!DOCTYPE html>
<html lang="en">
<head>
<meta charset="utf-8">
<title>Bright Ledger — Podcast Cover</title>
<link href="https://fonts.googleapis.com/css2?family=Righteous&family=Source+Sans+3:wght@400;600&family=Archivo:wght@400;700;900&display=swap" rel="stylesheet">
<style>
  :root {
    --sun: #f8c542;
    --sun-deep: #edbb42;
    --sun-shade: #e2af3e;
    --ink: #0b0b0b;
    --paper: #ffffff;
    --gold: #d9a535;
  }
  * { margin: 0; padding: 0; box-sizing: border-box; }
  html, body { width: 1200px; height: 1200px; overflow: hidden; background: var(--sun); }
  .cover { position: relative; width: 1200px; height: 1200px; background: var(--sun); overflow: hidden; }
  .cover__shapes { position: absolute; inset: 0; }
  .credit {
    position: absolute; right: 52px; top: 50px; text-align: right; color: var(--ink);
  }
  .credit__label {
    font-family: "Archivo", sans-serif; font-weight: 700; font-size: 34px;
    letter-spacing: 0.28em; margin-right: -0.28em; line-height: 1;
  }
  .credit__firm {
    font-family: "Source Sans 3", sans-serif; font-weight: 400; font-size: 39px;
    line-height: 1; margin-top: 10px;
  }
  .wordmark { position: absolute; left: 0; top: 0; width: 1200px; height: 700px; }
  .wordmark text { font-family: "Righteous", sans-serif; fill: var(--ink); }
  .rule {
    position: absolute; left: 317px; top: 816px; width: 567px; height: 3px; background: var(--ink);
  }
  .schedule {
    position: absolute; left: 0; width: 1200px; text-align: center; color: var(--ink);
    font-family: "Archivo", sans-serif; line-height: 1;
  }
  .schedule--lead { top: 864px; font-size: 38px; font-weight: 400; letter-spacing: 0.2em; }
  .schedule--day { top: 918px; font-size: 38px; font-weight: 700; letter-spacing: 0.2em; }
  .episode { position: absolute; right: 48px; top: 942px; text-align: right; font-family: "Archivo", sans-serif; }
  .episode__number { font-size: 186px; font-weight: 900; color: var(--gold); line-height: 0.8; letter-spacing: -0.02em; }
  .episode__label { font-size: 46px; font-weight: 900; color: var(--ink); letter-spacing: 0.16em; margin-right: -0.16em; margin-top: 10px; line-height: 1; }
</style>
</head>
<body>
<main class="cover">
  <svg class="cover__shapes" width="1200" height="1200" viewBox="0 0 1200 1200" aria-hidden="true">
    <path fill="var(--sun-shade)" d="M160 0 C230 100 330 140 470 130 C650 120 780 190 840 280 C930 400 980 440 1100 450 C1150 452 1180 440 1200 432 L1200 0 Z"/>
    <path fill="var(--sun-deep)" d="M160 0 C230 90 330 120 470 115 C650 110 780 170 840 260 C930 380 980 420 1100 430 C1150 432 1180 420 1200 412 L1200 0 Z"/>
    <path fill="var(--sun-shade)" d="M0 752 C90 720 160 720 180 800 C200 900 210 1000 320 1040 C450 1060 600 1060 720 1110 L720 1200 L0 1200 Z"/>
    <path fill="var(--sun-deep)" d="M0 770 C90 740 150 742 168 815 C188 915 200 1015 310 1058 C440 1080 590 1080 710 1130 L710 1200 L0 1200 Z"/>
    <path fill="var(--paper)" d="M670 1200 C670 1140 700 1090 760 1070 C860 1030 905 1000 925 940 C945 880 1000 840 1070 820 C1130 805 1170 815 1200 830 L1200 1200 Z"/>
  </svg>

  <header class="credit">
    <p class="credit__label">A PODCAST BY:</p>
    <p class="credit__firm">Thornbury Communications</p>
  </header>

  <svg class="wordmark" viewBox="0 0 1200 700" role="img" aria-label="Bright Ledger">
    <text x="95" y="438" font-size="270" textLength="820" lengthAdjust="spacingAndGlyphs">BRIGHT</text>
    <text x="101" y="665" font-size="270" textLength="1004" lengthAdjust="spacingAndGlyphs">LEDGER</text>
  </svg>

  <div class="rule"></div>
  <p class="schedule schedule--lead">NEW EPISODES</p>
  <p class="schedule schedule--day">EVERY FRIDAY</p>

  <div class="episode">
    <p class="episode__number">01</p>
    <p class="episode__label">EPISODE</p>
  </div>
</main>
</body>
</html>
```